We need a fresh, new church business card!!

We need a church business card with basic info to hand out as invites. We are looking for something clean that communicates our basic information clearly.

We are open to square or rectangle card sizes.

The attached logo is the only one that I have available. We'd like to see options with with text of the logo lighter and on a dark background as well as options with white/light backgrounds.

Also, we'd like to see option with rounded corners.

• Address - 2738 Larkmoor Ave., Fernbrook, IL 60947
• Website - brookvale.church
• Phone - 815-392-6157
• Service times -
• Sunday - 10am Sunday School
• - 11am Family Worship
• - 6pm Night of Prayer
• Wednesday - 7:30pm Adult Bible Study
• Classes for all ages

```html
<!DOCTYPE html>
<html lang="en">
<head>
<meta charset="utf-8">
<title>Brookvale Pentecostal Church – Business Card</title>
<link rel="stylesheet" href="https://fonts.googleapis.com/css2?family=Open+Sans:wght@400;600&display=swap">
<style>
  :root {
    --stage: #2e2a27;
    --card: #0b0b0b;
    --card-edge: #1c1c1c;
    --text: #e9e9e9;
    --muted: #bdbdbd;
    --brand-grey: #9a9a9a;
    --accent: #4f93a3;
    --divider: #3a3a3a;
  }
  * { box-sizing: border-box; margin: 0; padding: 0; }
  html, body { width: 1200px; height: 900px; overflow: hidden; }
  body {
    background: var(--stage);
    font-family: "Open Sans", Arial, sans-serif;
    display: flex;
    align-items: center;
    justify-content: center;
    gap: 40px;
  }
  .card {
    position: relative;
    width: 540px;
    height: 309px;
    background: var(--card);
    border: 1px solid var(--card-edge);
    display: flex;
    align-items: stretch;
  }
  .brand {
    width: 270px;
    display: flex;
    flex-direction: column;
    align-items: center;
    justify-content: center;
    gap: 14px;
    padding: 0 24px;
  }
  .brand-dot {
    width: 46px;
    height: 46px;
    border-radius: 50%;
    background: var(--accent);
  }
  .card--back .brand-dot { background: var(--muted); }
  .brand-name {
    font-weight: 400;
    font-size: 22px;
    line-height: 1.2;
    letter-spacing: 1px;
    text-transform: uppercase;
    text-align: center;
    color: var(--brand-grey);
  }
  .card--back .brand-name { color: var(--muted); }
  .divider {
    width: 1px;
    margin: 40px 0;
    background: var(--divider);
  }
  .info {
    flex: 1;
    padding: 44px 22px 0 26px;
    color: var(--text);
  }
  .address {
    font-size: 15px;
    line-height: 1.55;
    margin-bottom: 28px;
  }
  .contact-line {
    display: flex;
    align-items: center;
    gap: 10px;
    font-size: 15px;
    line-height: 1.6;
  }
  .contact-line svg { width: 12px; height: 12px; flex: none; }
  .service-title {
    font-size: 15px;
    color: var(--muted);
    margin-bottom: 14px;
  }
  .service-day {
    font-size: 15px;
    font-weight: 600;
    margin-bottom: 2px;
  }
  .service-list {
    list-style: none;
    font-size: 12px;
    line-height: 1.45;
    color: var(--muted);
    padding-left: 12px;
    margin-bottom: 14px;
  }
  .service-list strong { color: var(--text); font-weight: 600; }
  .classes {
    position: absolute;
    right: 28px;
    bottom: 30px;
    font-size: 15px;
    letter-spacing: 0.5px;
    color: var(--text);
  }
</style>
</head>
<body>

  <section class="card card--front" aria-label="Card front">
    <div class="brand">
      <span class="brand-dot"></span>
      <p class="brand-name">Brookvale Pentecostal Church</p>
    </div>
    <div class="divider"></div>
    <div class="info">
      <p class="address">2738 Larkmoor Ave., Fernbrook,<br>IL 60947</p>
      <p class="contact-line">
        <svg viewBox="0 0 12 12" aria-hidden="true"><path d="M2.5 1 L4.5 1 L5 3.5 L3.8 4.4 Q5 7 7.6 8.2 L8.5 7 L11 7.5 L11 9.5 Q10.5 11 9 11 Q1 10 1 2.5 Q1 1 2.5 1 Z" fill="var(--accent)"/></svg>
        815-392-6157
      </p>
      <p class="contact-line">
        <svg viewBox="0 0 12 12" aria-hidden="true"><circle cx="6" cy="6" r="5.5" fill="var(--accent)"/><path d="M0.5 6 H11.5 M6 0.5 Q3 6 6 11.5 M6 0.5 Q9 6 6 11.5" stroke="var(--card)" stroke-width="0.8" fill="none"/></svg>
        www.brookvale.church
      </p>
    </div>
  </section>

  <section class="card card--back" aria-label="Card back">
    <div class="brand">
      <span class="brand-dot"></span>
      <p class="brand-name">Brookvale Pentecostal Church</p>
    </div>
    <div class="divider"></div>
    <div class="info">
      <p class="service-title">Service Times</p>
      <p class="service-day">Sunday</p>
      <ul class="service-list">
        <li><strong>10am</strong> Sunday School</li>
        <li><strong>11am</strong> Family Worship</li>
        <li><strong>6pm</strong> Night of Prayer</li>
      </ul>
      <p class="service-day">Wednesday</p>
      <ul class="service-list">
        <li><strong>7:30pm</strong> Adult Bible Study</li>
      </ul>
    </div>
    <p class="classes">CLASSES FOR ALL AGES</p>
  </section>

</body>
</html>
```